BRIGHTWELL PROPERTY CHECKS Business card, please make it match the flyer.
Dana Pelworth
Dana@brightwellpropertychecksfl.example
555-218-7604 office
www.BrightwellPropertyChecks.example

Contact Information for Business Card

OUR LOGO

```html
<!DOCTYPE html>
<html lang="en">
<head>
<meta charset="utf-8">
<title>Brightwell Property Checks – Business Card</title>
<link rel="stylesheet" href="https://fonts.googleapis.com/css2?family=Poppins:wght@700&family=Roboto+Condensed:wght@400&display=swap">
<style>
  :root {
    --stage: #adadad;
    --card-light: #ffffff;
    --card-dark: #262626;
    --brand-red: #c4161c;
    --ink: #333333;
    --icon-navy: #1d3d6e;
    --divider: #d6d6d6;
    --on-dark: #ffffff;
  }
  * { margin: 0; padding: 0; box-sizing: border-box; }
  html, body { width: 1093px; height: 1200px; overflow: hidden; }
  body { background: var(--stage); position: relative; }

  .card {
    position: absolute;
    left: 265px;
    width: 578px;
    height: 356px;
    border-radius: 24px;
    overflow: hidden;
  }
  .card--front { top: 226px; background: var(--card-light); }
  .card--back  { top: 621px; background: var(--card-dark); }

  .brand {
    position: absolute;
    display: flex;
    align-items: center;
    gap: 10px;
    font-family: "Poppins", sans-serif;
    font-weight: 700;
    line-height: 1.15;
    letter-spacing: 0.5px;
  }
  .brand__dot { flex: none; border-radius: 50%; }
  .card--front .brand {
    left: 30px; top: 128px; width: 236px;
    color: var(--brand-red); font-size: 19px;
  }
  .card--front .brand__dot { width: 22px; height: 22px; background: var(--brand-red); }
  .card--back .brand {
    left: 0; right: 0; top: 146px; justify-content: center;
    color: var(--on-dark); font-size: 28px;
  }
  .card--back .brand__dot { width: 30px; height: 30px; background: var(--on-dark); }

  .divider {
    position: absolute;
    left: 287px; top: 90px;
    width: 1px; height: 176px;
    background: var(--divider);
  }

  .holder {
    position: absolute;
    left: 303px; top: 118px;
    font-family: "Poppins", sans-serif;
    font-weight: 700;
    font-size: 20px;
    color: var(--brand-red);
    letter-spacing: -0.2px;
    text-transform: uppercase;
  }

  .contact-list {
    position: absolute;
    left: 303px; top: 168px;
    list-style: none;
    font-family: "Roboto Condensed", sans-serif;
    font-size: 14.5px;
    color: var(--ink);
  }
  .contact-list li {
    display: flex; align-items: center; gap: 7px;
    height: 21px;
  }
  .contact-list svg { width: 15px; height: 15px; flex: none; fill: var(--icon-navy); }
</style>
</head>
<body>

<section class="card card--front" aria-label="Business card front">
  <div class="brand"><span class="brand__dot"></span><span>BRIGHTWELL PROPERTY CHECKS</span></div>
  <div class="divider"></div>
  <h1 class="holder">Dana Pelworth</h1>
  <ul class="contact-list">
    <li>
      <svg viewBox="0 0 24 24" aria-hidden="true"><path d="M6.6 10.8a15.1 15.1 0 0 0 6.6 6.6l2.2-2.2a1 1 0 0 1 1-.25 11.4 11.4 0 0 0 3.6.57 1 1 0 0 1 1 1V20a1 1 0 0 1-1 1A17 17 0 0 1 3 4a1 1 0 0 1 1-1h3.5a1 1 0 0 1 1 1c0 1.25.2 2.45.57 3.57a1 1 0 0 1-.25 1z"/></svg>
      <span>555-218-7604</span>
    </li>
    <li>
      <svg viewBox="0 0 24 24" aria-hidden="true"><path d="M2 5h20v14H2z M3.5 6.5v.4l8.5 6 8.5-6v-.4z" fill-rule="evenodd"/></svg>
      <span>Dana@brightwellpropertychecksfl.example</span>
    </li>
    <li>
      <svg viewBox="0 0 24 24" aria-hidden="true"><path d="M12 2a10 10 0 1 0 0 20 10 10 0 0 0 0-20zm6.9 6h-3a15.6 15.6 0 0 0-1.4-3.6A8 8 0 0 1 18.9 8zM12 4a14 14 0 0 1 1.9 4h-3.8A14 14 0 0 1 12 4zM4.3 14a8 8 0 0 1 0-4h3.4a16 16 0 0 0 0 4zm.8 2h3a15.6 15.6 0 0 0 1.4 3.6A8 8 0 0 1 5.1 16zm3-8h-3a8 8 0 0 1 4.4-3.6A15.6 15.6 0 0 0 8.1 8zM12 20a14 14 0 0 1-1.9-4h3.8A14 14 0 0 1 12 20zm2.3-6H9.7a14.7 14.7 0 0 1 0-4h4.6a14.7 14.7 0 0 1 0 4zm.2 5.6a15.6 15.6 0 0 0 1.4-3.6h3a8 8 0 0 1-4.4 3.6zm1.8-5.6a16 16 0 0 0 0-4h3.4a8 8 0 0 1 0 4z"/></svg>
      <span>www.BrightwellPropertyChecks.example</span>
    </li>
  </ul>
</section>

<section class="card card--back" aria-label="Business card back">
  <div class="brand"><span class="brand__dot"></span><span>BRIGHTWELL<br>PROPERTY CHECKS</span></div>
</section>

</body>
</html>
```